Clever & creative business card needed for a pediatric dentist.

We need a business card for a pediatric dentist that is building a brand-new pediatric dental practice. He is funny, outgoing, and sociable, and he hopes to give his business card to dentists and pediatricians so that he can give them information of where to refer infants, children, and teenagers that need high quality and attainable dental care.

The name of the dental practice is Amber Creek Pediatric Dentistry. Logo design .png / .pdf/ .jpg are provided to aid in the design.

The dentist's last name is Moffat (which sounds like "burger", as in "hamburger” or “cheeseburger"). Since it is pediatric practice, kudos will be given to designs that implement a little joke into the design - but hopefully in a small or hidden way (such as putting something like a cheeseburger on the back of the card, or hiding it an an abstract way).

Thank you!

Please make a design that incorporates colors. It should be fun! Not too serious. It does not have to follow the color scheme of the logos.

```html
<!DOCTYPE html>
<html lang="en">
<head>
<meta charset="utf-8">
<title>Amber Creek Pediatric Dentistry – Business Card</title>
<link rel="stylesheet" href="https://fonts.googleapis.com/css2?family=Poppins:wght@400;500;700&display=swap">
<style>
  :root {
    --backdrop: #2c2c2c;
    --card: #efefef;
    --card-shade: #e2e2e2;
    --ink: #333333;
    --green: #2e8b47;
    --green-soft: #9ec79f;
    --mark: #8cc793;
    --bun: #f1e2c6;
    --leaf: #d6ece0;
  }
  * { box-sizing: border-box; margin: 0; padding: 0; }
  html, body { width: 1200px; height: 1138px; overflow: hidden; }
  body {
    background: var(--backdrop);
    font-family: "Poppins", sans-serif;
    color: var(--ink);
    position: relative;
  }
  .card {
    position: absolute;
    width: 622px;
    height: 376px;
    border-radius: 16px;
    overflow: hidden;
    background: linear-gradient(180deg, var(--card) 0%, var(--card-shade) 100%);
  }
  .card--front { left: 272px; top: 184px; }
  .card--back { left: 274px; top: 606px; }

  .front-pattern {
    position: absolute; inset: 0;
    background:
      radial-gradient(ellipse at 10% 20%, var(--bun) 0 8%, transparent 14%),
      radial-gradient(ellipse at 90% 15%, var(--bun) 0 8%, transparent 14%),
      radial-gradient(ellipse at 30% 90%, var(--leaf) 0 7%, transparent 13%),
      radial-gradient(ellipse at 80% 88%, var(--bun) 0 7%, transparent 13%),
      linear-gradient(180deg, var(--card) 0%, var(--card-shade) 100%);
    opacity: .8;
  }
  .brand {
    position: absolute;
    display: flex; flex-direction: column; align-items: center;
    text-align: center;
  }
  .brand__dot {
    border-radius: 50%;
    background: var(--mark);
  }
  .brand__name {
    font-weight: 500;
    color: var(--ink);
    line-height: 1.15;
  }
  .card--front .brand { left: 0; right: 0; top: 92px; }
  .card--front .brand__dot { width: 84px; height: 84px; margin-bottom: 22px; }
  .card--front .brand__name { font-size: 38px; }

  .card--back .brand { left: 40px; width: 250px; top: 98px; }
  .card--back .brand__dot { width: 80px; height: 80px; margin-bottom: 18px; }
  .card--back .brand__name { font-size: 26px; }

  .contact {
    position: absolute; left: 351px; top: 68px;
  }
  .contact__name {
    font-weight: 700; font-size: 27px; color: var(--green);
    line-height: 1; letter-spacing: -0.3px;
  }
  .contact__role { font-size: 16px; margin-top: 6px; }
  .contact__list { list-style: none; margin-top: 24px; font-size: 16px; }
  .contact__list li { display: flex; align-items: center; height: 23px; }
  .contact__list svg { width: 14px; height: 14px; margin-right: 12px; fill: var(--green); }
  .contact__address { font-size: 16px; line-height: 23px; margin-top: 10px; }

  .footer-band { position: absolute; left: 0; bottom: 0; width: 622px; height: 48px; }
  .footer-band__label {
    position: absolute; left: 346px; bottom: 14px;
    font-size: 16px; color: #ffffff;
  }
</style>
</head>
<body>
  <section class="card card--front">
    <div class="front-pattern" role="img" aria-label="Faint scattered cheeseburger pattern"></div>
    <div class="brand">
      <span class="brand__dot"></span>
      <p class="brand__name">Amber Creek<br>Pediatric Dentistry</p>
    </div>
  </section>

  <section class="card card--back">
    <div class="brand">
      <span class="brand__dot"></span>
      <p class="brand__name">Amber Creek<br>Pediatric Dentistry</p>
    </div>

    <div class="contact">
      <h1 class="contact__name">OWEN MOFFAT</h1>
      <p class="contact__role">Managing Director</p>
      <ul class="contact__list">
        <li><svg viewBox="0 0 16 16"><path d="M1 5c0-2 3-3 7-3s7 1 7 3v2h-3V5H4v2H1zM4 8h8l2 6H2z"/></svg>000-0000-0000</li>
        <li><svg viewBox="0 0 16 16"><path d="M1 3h14v10H1zM2 4l6 5 6-5v1L8 10 2 5z" fill-rule="evenodd"/></svg>owen@ambercreek.com</li>
        <li><svg viewBox="0 0 16 16"><circle cx="8" cy="8" r="7" fill="none" stroke="#2e8b47" stroke-width="1.5"/><path d="M1 8h14M8 1c-3 3-3 11 0 14M8 1c3 3 3 11 0 14" fill="none" stroke="#2e8b47" stroke-width="1.2"/></svg>www.ambercreek.com</li>
      </ul>
      <p class="contact__address">234 Anywhere St., Any City,<br>Any Town, US 123456</p>
    </div>

    <svg class="footer-band" viewBox="0 0 622 48" aria-hidden="true">
      <rect x="0" y="32" width="300" height="16" fill="var(--green-soft)"/>
      <path d="M306 0H622V48H280Z" fill="var(--green)"/>
    </svg>
    <p class="footer-band__label">Amber Creek Pediatric Dentistry</p>
  </section>
</body>
</html>
```